We are an integrated facilities management company.

We aggregate everything related to facilities maintenance. Repair-replacement of equipment and facility space materials from:
Asset gathering and tracking.
Vendor screening, contracting and management.
Service requirement development.
Work order processing and management.
Invoice reconciliation.
Vendor payment.
Reporting.
Capital equipment bids and project management.

Target Market(s)

Retail, hospitality, multi-family housing, long term healthcare.

Industry/Entity Type

Maintenance

Contact Information for Business Card

Professional and bold look. (see logo zip file)

Colors
3377b5
85abd2
cedeed

Requirements
Must have
• N/A
Nice to have
• N/A
Should not have
• N/A

```html
<!DOCTYPE html>
<html lang="en">
<head>
<meta charset="utf-8">
<title>Steadfast Facility Group – Business Card</title>
<link rel="stylesheet" href="https://fonts.googleapis.com/css2?family=Montserrat:wght@400;500;600;700&display=swap">
<style>
  :root {
    --stage: #2b2d31;
    --card: #212428;
    --card-edge: #2a2d32;
    --brand-blue: #3377b5;
    --brand-sky: #85abd2;
    --brand-mist: #cedeed;
    --text-light: #e9edf2;
    --text-muted: #9aa3ad;
    --divider: #4a5058;
  }
  * { box-sizing: border-box; margin: 0; padding: 0; }
  html, body { width: 1200px; height: 800px; overflow: hidden; }
  body {
    background: var(--stage);
    font-family: "Montserrat", sans-serif;
    position: relative;
  }
  .card {
    position: absolute;
    top: 245px;
    width: 540px;
    height: 310px;
    border-radius: 18px;
    background: linear-gradient(160deg, var(--card-edge), var(--card));
    overflow: hidden;
    box-shadow: 0 18px 40px rgba(0,0,0,.45);
  }
  .card--back { left: 40px; }
  .card--front { left: 620px; }

  .brand {
    display: flex;
    align-items: center;
    gap: 12px;
  }
  .brand__mark {
    width: 38px; height: 38px;
    background: var(--brand-blue);
  }
  .brand__name {
    font-weight: 700;
    font-size: 20px;
    line-height: 1.05;
    letter-spacing: .5px;
    color: var(--brand-sky);
    text-transform: uppercase;
  }

  /* back: services */
  .card--back .brand { position: absolute; left: 36px; top: 34px; }
  .deco-block {
    position: absolute;
    right: 30px; top: 22px;
    width: 150px; height: 150px;
    background: rgba(255,255,255,.035);
  }
  .services {
    position: absolute;
    left: 40px; top: 100px;
    list-style: none;
  }
  .services li {
    display: flex;
    align-items: center;
    gap: 10px;
    font-size: 13px;
    font-weight: 500;
    color: var(--text-light);
    line-height: 23px;
  }
  .services svg { width: 12px; height: 12px; flex: none; }

  /* front: contact */
  .card--front .brand { position: absolute; left: 150px; top: 60px; }
  .card--front .brand__mark { width: 46px; height: 46px; }
  .card--front .brand__name { font-size: 23px; }
  .person {
    position: absolute;
    left: 70px; top: 168px;
    text-align: right;
    width: 170px;
  }
  .person__name {
    font-weight: 700; font-size: 17px; color: var(--text-light); letter-spacing: .5px;
  }
  .person__role {
    font-size: 12px; font-weight: 500; color: var(--brand-sky); letter-spacing: 1px; margin-top: 2px;
  }
  .contact-divider {
    position: absolute;
    left: 258px; top: 160px;
    width: 1px; height: 66px;
    background: var(--divider);
  }
  .contacts {
    position: absolute;
    left: 276px; top: 160px;
    list-style: none;
  }
  .contacts li {
    display: flex; align-items: center; gap: 8px;
    font-size: 12.5px; color: var(--text-light); line-height: 22px;
  }
  .contacts svg { width: 14px; height: 14px; flex: none; }
  .address-band {
    position: absolute;
    left: 0; bottom: 0;
    width: 100%; height: 44px;
    background: var(--brand-sky);
    border-top: 3px solid var(--brand-mist);
    display: flex; align-items: center; justify-content: center;
    font-size: 13px; font-weight: 600; color: #1b2430; letter-spacing: .3px;
  }
</style>
</head>
<body>

<section class="card card--back" aria-label="Card back: services">
  <div class="deco-block" aria-hidden="true"></div>
  <div class="brand">
    <span class="brand__mark" aria-hidden="true"></span>
    <span class="brand__name">Steadfast<br>Facility Group</span>
  </div>
  <ul class="services">
    <li><svg viewBox="0 0 12 12"><path d="M6 0v12M0 6h12M1.8 1.8l8.4 8.4M10.2 1.8l-8.4 8.4" stroke="#85abd2" stroke-width="1.4"/></svg>Asset gathering and tracking.</li>
    <li><svg viewBox="0 0 12 12"><path d="M6 0v12M0 6h12M1.8 1.8l8.4 8.4M10.2 1.8l-8.4 8.4" stroke="#85abd2" stroke-width="1.4"/></svg>Vendor screening, contracting and management.</li>
    <li><svg viewBox="0 0 12 12"><path d="M6 0v12M0 6h12M1.8 1.8l8.4 8.4M10.2 1.8l-8.4 8.4" stroke="#85abd2" stroke-width="1.4"/></svg>Service requirement development.</li>
    <li><svg viewBox="0 0 12 12"><path d="M6 0v12M0 6h12M1.8 1.8l8.4 8.4M10.2 1.8l-8.4 8.4" stroke="#85abd2" stroke-width="1.4"/></svg>Work order processing and management.</li>
    <li><svg viewBox="0 0 12 12"><path d="M6 0v12M0 6h12M1.8 1.8l8.4 8.4M10.2 1.8l-8.4 8.4" stroke="#85abd2" stroke-width="1.4"/></svg>Invoice reconciliation.</li>
    <li><svg viewBox="0 0 12 12"><path d="M6 0v12M0 6h12M1.8 1.8l8.4 8.4M10.2 1.8l-8.4 8.4" stroke="#85abd2" stroke-width="1.4"/></svg>Vendor payment.</li>
    <li><svg viewBox="0 0 12 12"><path d="M6 0v12M0 6h12M1.8 1.8l8.4 8.4M10.2 1.8l-8.4 8.4" stroke="#85abd2" stroke-width="1.4"/></svg>Reporting.</li>
    <li><svg viewBox="0 0 12 12"><path d="M6 0v12M0 6h12M1.8 1.8l8.4 8.4M10.2 1.8l-8.4 8.4" stroke="#85abd2" stroke-width="1.4"/></svg>Capital equipment bids and project management.</li>
  </ul>
</section>

<section class="card card--front" aria-label="Card front: contact">
  <div class="brand">
    <span class="brand__mark" aria-hidden="true"></span>
    <span class="brand__name">Steadfast<br>Facility Group</span>
  </div>
  <div class="person">
    <p class="person__name">JORDAN REYES</p>
    <p class="person__role">OWNER</p>
  </div>
  <div class="contact-divider" aria-hidden="true"></div>
  <ul class="contacts">
    <li><svg viewBox="0 0 14 14"><circle cx="7" cy="7" r="6.3" fill="none" stroke="#cedeed" stroke-width="1.2"/><path d="M5 3.8l1 1.6-.7.8c.4.9 1 1.6 1.9 2l.8-.7 1.6 1-.6 1.2c-2.3-.3-4.3-2.3-4.6-4.7z" fill="#cedeed"/></svg>555.010.2040</li>
    <li><svg viewBox="0 0 14 14"><circle cx="7" cy="7" r="6.3" fill="none" stroke="#cedeed" stroke-width="1.2"/><rect x="3.8" y="4.8" width="6.4" height="4.4" fill="none" stroke="#cedeed" stroke-width="1"/><path d="M3.8 4.8L7 7.4l3.2-2.6" fill="none" stroke="#cedeed" stroke-width="1"/></svg>hello@steadfastfg.com</li>
    <li><svg viewBox="0 0 14 14"><circle cx="7" cy="7" r="6.3" fill="none" stroke="#cedeed" stroke-width="1.2"/><circle cx="7" cy="7" r="3.4" fill="none" stroke="#cedeed" stroke-width="1"/><path d="M3.6 7h6.8M7 3.6v6.8" stroke="#cedeed" stroke-width="1"/></svg>www.steadfastfg.com</li>
  </ul>
  <div class="address-band">PO BOX 482, Harbor Road, Suite 4, Arizona 85001</div>
</section>

</body>
</html>
```